Wordpress Design Project for Bankruptcy Law Office in San Francisco

our current website: www.dorvanelilaw.example

we would like to re-design it for wordpress to make it faster and a bit more modern.

content should be similar to what we have there right now but also we do family law

please include logo for law office:

Law Office of Marta K. Dorvaneli

Thank you.
Updates

please see attached word document with logos that we like as an example.

we do tend to like color red.  darker red.

Please submit your design variations and logo as soon as possible.   We would like to go over them and make our decision

Reason: Please create couple of more variations of logo for your design, so we can make our decision what we like the most. Please see word doc for samples: Text: Law Office Of Marta K. Dorvaneli

Reason: final touches

Target Market(s)

bankruptcy and family law clients

Industry/Entity Type

Family Law

Requirements
Must have
• see examples of law sites
http://marketing.lexoriba.example/testimonials

- new logo: Law Office of Marta K. Dorvaneli
- client intake form
- blog
- contact us form

Nice to have
• - map
- red color
- on the front page a nice photo of SF or a happy family

```html
<!DOCTYPE html>
<html lang="en">
<head>
<meta charset="utf-8">
<title>Law Office of Marta K. Dorvaneli</title>
<link href="https://fonts.googleapis.com/css2?family=PT+Sans:ital,wght@0,400;0,700;1,400&display=swap" rel="stylesheet">
<style>
:root{
  --page:#f4f4f4;
  --panel:#ffffff;
  --red:#c0140c;
  --red-dark:#8e0c08;
  --red-text:#b5120c;
  --gold:#c9a25c;
  --ink:#333333;
  --body:#555555;
  --muted:#999999;
  --line:#d5d5d5;
}
*{box-sizing:border-box;margin:0;padding:0}
html,body{width:1188px;height:1200px;overflow:hidden}
body{background:var(--page);font-family:"PT Sans",Arial,sans-serif;color:var(--ink);position:relative}
.abs{position:absolute}
.top-rule{left:0;top:0;width:1188px;height:7px;background:var(--red)}
.brand{left:72px;top:23px;display:flex;align-items:center;gap:16px}
.brand-mark{width:80px;height:80px;border-radius:50%;background:radial-gradient(circle at 40% 35%,#e6c98d,var(--gold) 60%,#a9803d)}
.brand-name{font-size:27px;font-weight:700;color:var(--red-dark);line-height:32px;letter-spacing:.5px}
.search{left:920px;top:54px;width:195px;height:27px;background:#fff;border:1px solid #cfcfcf;box-shadow:0 1px 3px rgba(0,0,0,.15);font-size:12px;font-style:italic;color:#aaa;padding:5px 15px}
.search svg{position:absolute;right:7px;top:7px}
.nav-band{left:0;top:136px;width:1188px;height:30px;background:var(--red)}
.nav{left:73px;top:124px;width:1044px;height:52px;display:flex;background:linear-gradient(#d11d12,#a80e08);border-radius:3px 3px 0 0;box-shadow:0 2px 3px rgba(0,0,0,.25)}
.nav a{color:#fff;text-decoration:none;font-size:14px;display:flex;align-items:center;justify-content:center;border-right:1px solid rgba(0,0,0,.18);box-shadow:inset -1px 0 rgba(255,255,255,.12)}
.nav a:last-child{border:none;box-shadow:none}
.nav a.active{background:linear-gradient(#c81a10,#b31109)}
.slider{left:72px;top:186px;width:1045px;height:323px;border:3px solid #d8d8d8;background:#fff}
.slide-photo{position:absolute;inset:0;background:linear-gradient(100deg,#b4aaa6 0%,#a09591 45%,#6e5c52 70%,#4c3a31 100%)}
.slide-title{position:absolute;left:77px;top:80px;font-size:31px;color:#333;letter-spacing:-.3px}
.dots{position:absolute;left:27px;top:283px;display:flex;gap:12px}
.dots span{width:11px;height:11px;border-radius:50%;background:#444}
.dots span.on{background:#8e0c08}
.panel{left:72px;top:523px;width:1046px;height:593px;background:var(--panel)}
.h2{font-size:22px;font-weight:400;color:var(--red-text);letter-spacing:-.2px}
.welcome-title{left:93px;top:548px}
.welcome-text{left:93px;top:590px;width:714px;font-size:13px;line-height:24px;color:var(--body);text-align:justify}
.person{left:788px;top:529px;width:330px;height:303px;background:linear-gradient(90deg,#fff 0%,#eef0f5 30%,#dfe2ea 60%,#fff 100%)}
.ticks{top:728px;list-style:none;font-size:13px;color:var(--ink)}
.ticks li{height:28px;display:flex;align-items:center;gap:13px}
.ticks svg{flex:none}
.rule{left:93px;top:861px;width:1004px;height:1px;background:var(--line)}
.news-title{left:93px;top:886px}
.about-title{left:634px;top:886px}
.dotted{top:931px;height:0;border-top:2px dotted #b5b5b5}
.news-item{left:93px;width:504px;display:flex;gap:17px}
.news-icon{flex:none;width:34px;height:34px;border-radius:50%;background:#dcdcdc;margin-top:7px;display:flex;align-items:center;justify-content:center}
.news-item p,.about-text{font-size:12.5px;line-height:19.5px;color:var(--body);text-align:justify}
.date{font-style:italic;color:var(--red-text)}
.about-text{left:634px;top:952px;width:277px}
.about-photo{left:928px;top:956px;width:169px;height:111px;border-radius:3px;background:radial-gradient(circle at 50% 40%,#d9bb85,#b48e55 60%,#8a6a3c)}
.more{left:634px;top:1057px;font-size:12.5px;font-style:italic;color:var(--red-text)}
.footer-links{left:72px;top:1135px;font-size:12.5px;color:#444}
.footer-links span{color:#888;margin:0 6px}
.copy{left:72px;top:1161px;font-size:12.5px;color:#444}
.social{top:1142px;width:33px;height:33px;border-radius:50%;background:#9a9a9a}
</style>
</head>
<body>
<div class="abs top-rule"></div>

<div class="abs brand">
  <div class="brand-mark"></div>
  <div class="brand-name">Law Office of<br>Marta K. Dorvaneli</div>
</div>

<div class="abs search">Search
  <svg width="12" height="12" viewBox="0 0 12 12"><circle cx="5" cy="5" r="3.5" fill="none" stroke="#aaa" stroke-width="1.4"/><line x1="7.6" y1="7.6" x2="11" y2="11" stroke="#aaa" stroke-width="1.6"/></svg>
</div>

<div class="abs nav-band"></div>
<nav class="abs nav">
  <a class="active" style="width:108px" href="#">HOME</a>
  <a style="width:123px" href="#">ABOUT US</a>
  <a style="width:116px" href="#">LAWYERS</a>
  <a style="width:141px" href="#">LATEST NEWS</a>
  <a style="width:162px" href="#">LATEST ARTICLES</a>
  <a style="width:162px" href="#">PRACTICE AREAS</a>
  <a style="width:136px" href="#">CONTACT US</a>
  <a style="width:96px" href="#">FAQ</a>
</nav>

<div class="abs slider">
  <div class="slide-photo" role="img" aria-label="Photo of a wooden judge's gavel on its sound block"></div>
  <div class="slide-title">DUIS AUTE IRURE DOLOR</div>
  <div class="dots"><span class="on"></span><span></span><span></span><span></span></div>
</div>

<div class="abs panel"></div>
<div class="abs person" role="img" aria-label="Photo of a smiling lawyer in shirt and tie leaning on a desk"></div>

<h2 class="abs h2 welcome-title">WELCOME TO OUR SITE</h2>
<p class="abs welcome-text">Sed ut perspiciatis unde omnis iste natus error sit voluptatem accusantium doloremque laudantium, totam rem aperiam, eaque ipsa quae ab illo inventore veritatis et quasi architecto beatae vitae dicta sunt explicabo. Nemo enim ipsam voluptatem quia voluptas sit aspernatur aut odit aut fugit, sed quia consequuntur magni dolores eos qui ratione voluptatem sequi nesciunt. Neque porro quisquam est, qui dolorem ipsum quia dolor sit amet, consectetur, adipisci velit, sed quia non numquam eius modi tempora incidunt ut labore et dolore magnam aliquam.</p>

<ul class="abs ticks" style="left:126px">
  <li><svg width="12" height="12" viewBox="0 0 12 12"><circle cx="6" cy="6" r="6" fill="#555"/><path d="M3 6h5M6 3.5 8.5 6 6 8.5" stroke="#fff" stroke-width="1.4" fill="none"/></svg>Duis accumsan aliquet arcu, vitae</li>
  <li><svg width="12" height="12" viewBox="0 0 12 12"><circle cx="6" cy="6" r="6" fill="#555"/><path d="M3 6h5M6 3.5 8.5 6 6 8.5" stroke="#fff" stroke-width="1.4" fill="none"/></svg>Morbi non lacus scelerisque nisl rhoncus</li>
  <li><svg width="12" height="12" viewBox="0 0 12 12"><circle cx="6" cy="6" r="6" fill="#555"/><path d="M3 6h5M6 3.5 8.5 6 6 8.5" stroke="#fff" stroke-width="1.4" fill="none"/></svg>Pellentesque pellentesque</li>
  <li><svg width="12" height="12" viewBox="0 0 12 12"><circle cx="6" cy="6" r="6" fill="#555"/><path d="M3 6h5M6 3.5 8.5 6 6 8.5" stroke="#fff" stroke-width="1.4" fill="none"/></svg>Cras venenatis massa ut orci pretium sit</li>
</ul>
<ul class="abs ticks" style="left:451px">
  <li><svg width="12" height="12" viewBox="0 0 12 12"><circle cx="6" cy="6" r="6" fill="#555"/><path d="M3 6h5M6 3.5 8.5 6 6 8.5" stroke="#fff" stroke-width="1.4" fill="none"/></svg>Duis accumsan aliquet arcu, vitae</li>
  <li><svg width="12" height="12" viewBox="0 0 12 12"><circle cx="6" cy="6" r="6" fill="#555"/><path d="M3 6h5M6 3.5 8.5 6 6 8.5" stroke="#fff" stroke-width="1.4" fill="none"/></svg>Morbi non lacus scelerisque nisl rhoncus</li>
  <li><svg width="12" height="12" viewBox="0 0 12 12"><circle cx="6" cy="6" r="6" fill="#555"/><path d="M3 6h5M6 3.5 8.5 6 6 8.5" stroke="#fff" stroke-width="1.4" fill="none"/></svg>Pellentesque pellentesque</li>
  <li><svg width="12" height="12" viewBox="0 0 12 12"><circle cx="6" cy="6" r="6" fill="#555"/><path d="M3 6h5M6 3.5 8.5 6 6 8.5" stroke="#fff" stroke-width="1.4" fill="none"/></svg>Cras venenatis massa ut orci pretium sit</li>
</ul>

<div class="abs rule"></div>

<h2 class="abs h2 news-title">LATEST NEWS</h2>
<div class="abs dotted" style="left:93px;width:504px"></div>
<div class="abs news-item" style="top:952px">
  <div class="news-icon"><svg width="16" height="16" viewBox="0 0 16 16"><rect x="1" y="1" width="11" height="11" fill="none" stroke="#fff" stroke-width="1.6"/><rect x="4" y="4" width="11" height="11" fill="#fff"/></svg></div>
  <p>Sed ut perspiciatis unde omnis iste natus error sit voluptatem accusantium dolor emque laudantium, totam rem aperiam, eaque ipsa quae ab illo inventore veritatis<br><span class="date">August 29th, 2012</span></p>
</div>
<div class="abs news-item" style="top:1029px">
  <div class="news-icon"><svg width="16" height="16" viewBox="0 0 16 16"><rect x="1" y="1" width="11" height="11" fill="none" stroke="#fff" stroke-width="1.6"/><rect x="4" y="4" width="11" height="11" fill="#fff"/></svg></div>
  <p>Sed ut perspiciatis unde omnis iste natus error sit voluptatem accusantium dolor emque laudantium, totam rem aperiam, eaque ipsa quae ab illo inventore veritatis<br><span class="date">August 29th, 2012</span></p>
</div>

<h2 class="abs h2 about-title">ABOUT US</h2>
<div class="abs dotted" style="left:634px;width:463px"></div>
<p class="abs about-text">Sed ut perspiciatis unde omnis iste natus error sit voluptatem accusantium dolor emque laudantium, totam rem aperiam, eaque ipsa quae ab illo inven-voluptatum deleniti atque corrupti quos dolores et quas molestias excepturi sint occaecati cupiditate</p>
<div class="abs about-photo" role="img" aria-label="Photo of a bronze statue of Lady Justice holding scales"></div>
<a class="abs more">View more</a>

<div class="abs footer-links">Home<span>|</span>About us<span>|</span>Lawyers<span>|</span>Latest News<span>|</span>Latest Articles<span>|</span>Practice Areas<span>|</span>Contact us<span>|</span>FAQ</div>
<div class="abs copy">Copyright © 2012 www.dorvanelilaw.example&nbsp;&nbsp;&nbsp;&nbsp;All rights reserved.</div>
<div class="abs social" style="left:1024px"></div>
<div class="abs social" style="left:1071px"></div>
</body>
</html>
```